Create modern and sleek business card for luxury real estate company

We're a "boutique" real estate office looking for a design that gets across a highly modern luxury brand. Blacks and whites are probably the best colors unless we try a silver foil for the logo. I've attached a version of our current logo here. I'd like to swap out the current font on there with Gotham Light Regular.

I'm looking to have one side of the card have the logo with the space for our agents info on the other side.

Target Market(s)

Young professionals in a "luxury" headspace

Industry/Entity Type

Real estate

Contact Information for Business Card

A place for agent name, cell number, website. The slogan "Quietly Redefining Fine Homes".

Font styles to use
Other font styles liked:
• Gotham Regular

Colors

Designer to choose only greyscale colors for use in the design.

Requirements
Must have
• Matte black as the background color. Clean lines and use of contrast. A specific design aspect that will use silver foil.
Nice to have
• Up in the air on integrating a QR code
Should not have
• Any houses or other real estate related design (ex: a clip art house)

```html
<!DOCTYPE html>
<html lang="en">
<head>
<meta charset="utf-8">
<title>Halden Realty – Business Card</title>
<link href="https://fonts.googleapis.com/css2?family=Montserrat:wght@300;500;700&display=swap" rel="stylesheet">
<style>
  :root {
    --backdrop: #24282d;
    --card-black: #2e3134;
    --emboss: #3a3e42;
    --emboss-line: #43474b;
    --silver: #e6e7e8;
    --silver-soft: #cfd1d3;
  }
  * { margin: 0; padding: 0; box-sizing: border-box; }
  html, body {
    width: 1200px; height: 1200px; overflow: hidden;
    background: var(--backdrop);
    font-family: "Montserrat", sans-serif;
  }
  .canvas {
    width: 1200px; height: 1200px;
    display: flex; flex-direction: column; align-items: center;
    justify-content: center; gap: 52px;
  }
  .card {
    position: relative;
    width: 900px; height: 514px;
    background: var(--card-black);
  }

  /* Front: agent details with embossed company name */
  .emboss-mark {
    position: absolute; left: 110px; top: 70px;
    display: flex; align-items: center; gap: 40px;
    color: var(--emboss);
  }
  .emboss-mark .mark-circle {
    width: 190px; height: 190px; border-radius: 50%;
    border: 4px solid var(--emboss-line);
    flex: none;
  }
  .emboss-mark .mark-name {
    font-weight: 300; font-size: 92px; line-height: 0.98;
    letter-spacing: 2px; text-transform: uppercase;
  }
  .agent-name {
    position: absolute; left: 110px; top: 340px;
    color: var(--silver);
    font-weight: 700; font-size: 54px; line-height: 1.02;
  }
  .agent-contact {
    position: absolute; left: 400px; top: 370px;
    list-style: none;
    color: var(--silver-soft);
    font-weight: 500; font-size: 21px; line-height: 1.75;
    letter-spacing: 0.5px;
  }

  /* Back: brand side */
  .brand-lockup {
    position: absolute; left: 250px; top: 110px;
    display: flex; align-items: center; gap: 26px;
    color: var(--silver);
  }
  .brand-lockup .mark-circle {
    width: 120px; height: 120px; border-radius: 50%;
    border: 4px solid var(--silver);
    flex: none;
  }
  .brand-lockup .mark-name {
    font-weight: 300; font-size: 58px; line-height: 1.05;
    letter-spacing: 1.5px; text-transform: uppercase;
  }
  .slogan {
    position: absolute; left: 110px; bottom: 70px;
    color: var(--silver-soft);
    font-weight: 700; font-size: 30px; letter-spacing: 0.5px;
  }
</style>
</head>
<body>
<main class="canvas">
  <section class="card card-front" aria-label="Business card front">
    <div class="emboss-mark" aria-hidden="true">
      <span class="mark-circle"></span>
      <span class="mark-name">Halden<br>Realty</span>
    </div>
    <h1 class="agent-name">Agent<br>Name</h1>
    <ul class="agent-contact">
      <li>555 214 7730</li>
      <li>info@haldenrealty.com</li>
      <li>www.haldenrealty.com</li>
    </ul>
  </section>

  <section class="card card-back" aria-label="Business card back">
    <div class="brand-lockup">
      <span class="mark-circle"></span>
      <span class="mark-name">Halden<br>Realty</span>
    </div>
    <p class="slogan">Quietly Redefining Fine Homes</p>
  </section>
</main>
</body>
</html>
```